Flyer Design for an electrical and security company trying to build local customers

I need a flyer design for a new company based in Sans Souci, Sydney 2219 called "Harbor Quill Dune Electrical and Security" also "HQD Electrical and Security". We are electrical contractors who are looking for more local work including emergency service calls and any project work including renovations or new constructions in the local area. I would like everyone in the area to know I am new and that I am available 24 hours a day 7 days a week. I would like to see designs that use the logo colours. Would also like the font of the entire design to be "juice bold".

Electrical

• juice bold

Requirements
Must have
• Must use the colours of the original logo and also have the information from the rear of the card. Must also have services buttons like the website picture attached.

```html
<!DOCTYPE html>
<html lang="en">
<head>
<meta charset="utf-8">
<title>Harbor Quill Dune Electrical and Security – Flyer</title>
<link href="https://fonts.googleapis.com/css2?family=Exo+2:wght@500;600;700&display=swap" rel="stylesheet">
<style>
  :root {
    --backdrop: #3f2d22;
    --paper: #ffffff;
    --ink: #111111;
    --sky: #66e3fb;
    --coral: #f47a4f;
    --icon-ring: #222222;
  }
  * { box-sizing: border-box; margin: 0; padding: 0; }
  html, body { width: 1200px; height: 900px; overflow: hidden; }
  body {
    background: var(--backdrop);
    font-family: "Exo 2", sans-serif;
    color: var(--ink);
    position: relative;
  }
  .page { position: absolute; top: 40px; width: 587px; height: 828px; overflow: hidden; }
  .page--front { left: 8px; background: var(--paper); }
  .page--back { left: 603px; background: var(--sky); }

  .brand-name {
    position: absolute; left: 92px; top: 48px;
    font-weight: 700; font-size: 60px; line-height: 0.95;
    color: var(--ink); letter-spacing: 1px;
  }
  .brand-tagline {
    position: absolute; left: 94px; top: 240px;
    font-weight: 600; font-size: 23px; letter-spacing: 0.5px;
  }
  .hero-art {
    position: absolute; left: 0; top: 300px; width: 587px; height: 528px;
    background: linear-gradient(160deg, var(--coral) 0%, #b4573a 40%, var(--ink) 75%);
  }
  .availability {
    position: absolute; left: 410px; top: 688px; width: 118px;
    text-align: center; color: var(--sky); font-weight: 600;
  }
  .availability__hours { font-size: 34px; line-height: 1; padding-bottom: 6px; border-bottom: 2px solid var(--coral); }
  .availability__label { font-size: 32px; line-height: 1.15; }

  .services-title {
    position: absolute; top: 32px; width: 100%; text-align: center;
    font-weight: 700; font-size: 26px; letter-spacing: 1.5px;
  }
  .service { position: absolute; width: 130px; margin-left: -65px; text-align: center; }
  .service__icon {
    display: flex; align-items: center; justify-content: center;
    width: 54px; height: 54px; margin: 0 auto 12px;
    border-radius: 50%; background: var(--paper); border: 2px solid var(--icon-ring);
  }
  .service__icon svg { width: 30px; height: 30px; }
  .service__icon--accent { background: var(--coral); }
  .service__label { font-size: 13px; font-weight: 600; line-height: 1.07; letter-spacing: 0.4px; }

  .contact-rule { position: absolute; left: 0; top: 674px; width: 100%; height: 2px; background: var(--coral); }
  .contact {
    position: absolute; top: 686px; width: 100%; text-align: center;
    font-weight: 600; font-size: 18px; line-height: 23px; letter-spacing: 0.8px;
  }
</style>
</head>
<body>
  <section class="page page--front">
    <div class="brand-name">harbor<br>quill<br>dune</div>
    <div class="brand-tagline">electrical and security</div>
    <div class="hero-art" role="img" aria-label="Angular lightning-bolt graphic in coral, sky blue and black rising across the lower page"></div>
    <div class="availability">
      <div class="availability__hours">24/7</div>
      <div class="availability__label">Service</div>
    </div>
  </section>

  <section class="page page--back">
    <h1 class="services-title">OUR SERVICES</h1>

    <div class="service" style="left:103px;top:86px">
      <span class="service__icon service__icon--accent"><svg viewBox="0 0 30 30" aria-hidden="true"><circle cx="15" cy="15" r="10" fill="none" stroke="#fff" stroke-width="2"/><path d="M15 9v6l4 3" fill="none" stroke="#fff" stroke-width="2" stroke-linecap="round"/></svg></span>
      <div class="service__label">24 hour<br>emergency<br>service</div></div>
    <div class="service" style="left:228px;top:86px">
      <span class="service__icon"><svg viewBox="0 0 30 30" aria-hidden="true"><path d="M6 6l18 18M24 6L6 24" stroke="var(--ink)" stroke-width="4" stroke-linecap="round"/></svg></span>
      <div class="service__label">new<br>installations</div></div>
    <div class="service" style="left:355px;top:86px">
      <span class="service__icon"><svg viewBox="0 0 30 30" aria-hidden="true"><path d="M4 15L15 5l11 10M8 13v12h14V13" fill="none" stroke="var(--ink)" stroke-width="2"/></svg></span>
      <div class="service__label">repairs</div></div>
    <div class="service" style="left:485px;top:86px">
      <span class="service__icon"><svg viewBox="0 0 30 30" aria-hidden="true"><path d="M4 15L15 5l11 10v11H4z" fill="var(--ink)"/><rect x="12" y="17" width="6" height="9" fill="#fff"/></svg></span>
      <div class="service__label">maintenance</div></div>

    <div class="service" style="left:103px;top:231px">
      <span class="service__icon"><svg viewBox="0 0 30 30" aria-hidden="true"><path d="M3 15L15 5l12 10v11H3z" fill="var(--ink)"/><rect x="8" y="17" width="4" height="4" fill="#fff"/><rect x="18" y="17" width="4" height="4" fill="#fff"/></svg></span>
      <div class="service__label">renovations/<br>extensions</div></div>
    <div class="service" style="left:228px;top:231px">
      <span class="service__icon"><svg viewBox="0 0 30 30" aria-hidden="true"><path d="M5 25c6-4 6-10 8-16M10 25c5-4 7-9 11-13M15 25c4-3 6-6 10-8" fill="none" stroke="var(--ink)" stroke-width="2"/></svg></span>
      <div class="service__label">re-wiring</div></div>
    <div class="service" style="left:355px;top:231px">
      <span class="service__icon"><svg viewBox="0 0 30 30" aria-hidden="true"><rect x="7" y="5" width="16" height="11" fill="none" stroke="var(--ink)" stroke-width="2"/><rect x="3" y="19" width="24" height="6" fill="var(--ink)"/></svg></span>
      <div class="service__label">home theatre</div></div>
    <div class="service" style="left:485px;top:231px">
      <span class="service__icon"><svg viewBox="0 0 30 30" aria-hidden="true"><rect x="3" y="7" width="10" height="17" fill="var(--ink)"/><rect x="17" y="7" width="10" height="17" fill="var(--ink)"/><circle cx="8" cy="18" r="3" fill="#fff"/><circle cx="22" cy="18" r="3" fill="#fff"/></svg></span>
      <div class="service__label">surround sound</div></div>

    <div class="service" style="left:103px;top:378px">
      <span class="service__icon"><svg viewBox="0 0 30 30" aria-hidden="true"><rect x="3" y="8" width="24" height="16" rx="2" fill="none" stroke="var(--ink)" stroke-width="2.5"/><path d="M12 8l3-4 3 4" fill="none" stroke="var(--ink)" stroke-width="1.5"/></svg></span>
      <div class="service__label">wall tv's</div></div>
    <div class="service" style="left:228px;top:378px">
      <span class="service__icon"><svg viewBox="0 0 30 30" aria-hidden="true"><path d="M4 8h10l4 4v4h-6v-4H4z" fill="var(--ink)"/><circle cx="18" cy="21" r="1.5" fill="var(--ink)"/><circle cx="22" cy="24" r="1.5" fill="var(--ink)"/><circle cx="16" cy="25" r="1.5" fill="var(--ink)"/></svg></span>
      <div class="service__label">electric<br>hot water</div></div>
    <div class="service" style="left:355px;top:378px">
      <span class="service__icon"><svg viewBox="0 0 30 30" aria-hidden="true"><rect x="6" y="8" width="18" height="10" rx="2" fill="var(--ink)"/><path d="M3 9h3M24 9h3" stroke="var(--ink)" stroke-width="2"/><path d="M15 20c-3 3 0 6 0 6s3-3 0-6z" fill="var(--ink)"/></svg></span>
      <div class="service__label">stoves</div></div>
    <div class="service" style="left:485px;top:378px">
      <span class="service__icon"><svg viewBox="0 0 30 30" aria-hidden="true"><rect x="5" y="6" width="20" height="18" rx="2" fill="var(--ink)"/><path d="M8 26v2M22 26v2" stroke="var(--ink)" stroke-width="2"/></svg></span>
      <div class="service__label">cooktops</div></div>

    <div class="service" style="left:165px;top:533px">
      <span class="service__icon"><svg viewBox="0 0 30 30" aria-hidden="true"><path d="M6 24L24 6M10 24L24 10M6 6l18 18" stroke="var(--ink)" stroke-width="2.5" stroke-linecap="round"/></svg></span>
      <div class="service__label">lighting &amp;<br>ceiling fans</div></div>
    <div class="service" style="left:293px;top:533px">
      <span class="service__icon"><svg viewBox="0 0 30 30" aria-hidden="true"><path d="M4 12c0-7 22-7 22 0v3h-6v-2c-3-1-7-1-10 0v2H4z M7 16h16l3 9H4z" fill="var(--ink)"/><circle cx="15" cy="20.5" r="2.5" fill="#fff"/></svg></span>
      <div class="service__label">telephone</div></div>
    <div class="service" style="left:425px;top:533px">
      <span class="service__icon"><svg viewBox="0 0 30 30" aria-hidden="true"><path d="M4 10l18 5-2 5-18-5z" fill="var(--ink)"/><path d="M20 19l2 6h4" fill="none" stroke="var(--ink)" stroke-width="2"/></svg></span>
      <div class="service__label">security<br>systems</div></div>

    <div class="contact-rule"></div>
    <div class="contact">
      <p>Schedule your Work Service</p>
      <p>Call Us Today</p>
      <p>1300 555 019</p>
    </div>
  </section>
</body>
</html>
```